heating and plumbing engineer needing a business card

business card for me about to go self employed, i am a gas heating engineer in the UK and will be undertaking all boiler installation, servicing, breakdown and repair work. i specialize in Brenhurst boilers and would like the brenhurst logo to appear on the card somewhere along with the words "Brenhurst Specialist"
The company will be called Quellin Heating and Plumbing, i chose quellin as it means to understand, comprehend, work out, quellin out, make sense of a problem.
must include contact email address quellinheating@mailvora.net
mobile number 07832 480917
my name derek hollis

```html
<!DOCTYPE html>
<html lang="en">
<head>
<meta charset="utf-8">
<title>Quellin Heating and Plumbing – Business Card Options</title>
<link rel="stylesheet" href="https://fonts.googleapis.com/css2?family=Oswald:wght@500;600&family=Roboto+Condensed:wght@300;400&family=Arimo&display=swap">
<style>
  :root {
    --teal: #00876f;
    --ink: #2b2b2b;
    --swoosh: #2a2a2a;
    --sheet: #e9eaea;
    --card: #ffffff;
    --label: #333333;
  }
  * { margin: 0; padding: 0; box-sizing: border-box; }
  html, body { width: 1200px; height: 2172px; overflow: hidden; }
  body { background: var(--sheet); position: relative; font-family: "Roboto Condensed", sans-serif; color: var(--ink); }

  .option-number { position: absolute; left: 42px; width: 30px; text-align: center; font-family: "Arimo", sans-serif; font-size: 43px; color: var(--label); }

  .card { position: absolute; width: 964px; height: 595px; background: var(--card); box-shadow: 0 4px 14px rgba(0,0,0,0.22); overflow: hidden; }

  .company-name { font-family: "Oswald", sans-serif; font-weight: 600; font-size: 58px; color: #fff; letter-spacing: 0.5px; white-space: nowrap; }
  .holder-name { font-family: "Oswald", sans-serif; font-weight: 600; font-size: 32px; color: var(--ink); }

  .brand-line { display: flex; align-items: flex-end; gap: 12px; }
  .brand-mark { display: flex; align-items: center; gap: 8px; font-family: "Oswald", sans-serif; font-weight: 600; font-size: 56px; line-height: 1; color: var(--teal); }
  .brand-square { width: 38px; height: 38px; background: var(--teal); }
  .brand-role { font-family: "Roboto Condensed", sans-serif; font-weight: 400; font-size: 36px; line-height: 1.15; color: var(--ink); }

  .contact-line { display: flex; align-items: center; gap: 14px; font-weight: 300; font-size: 31px; color: var(--ink); }
  .contact-icon { width: 30px; height: 26px; flex: none; }
  .contact-icon path, .contact-icon rect { fill: none; stroke: var(--teal); stroke-width: 2.6; }

  /* Option 1 */
  .card-wave { left: 123px; top: 92px; }
  .card-wave .wave { position: absolute; inset: 0; width: 100%; height: 100%; }
  .card-wave .details { position: absolute; left: 101px; top: 122px; display: flex; flex-direction: column; gap: 14px; }
  .card-wave .company-name { position: absolute; left: 0; right: 0; top: 462px; text-align: center; padding-left: 90px; }

  /* Options 2 & 3 */
  .header-band { position: absolute; left: 0; top: 0; width: 100%; height: 157px; background: var(--teal); display: flex; align-items: center; justify-content: center; padding-top: 6px; }
  .centre-stack { position: absolute; left: 0; right: 0; display: flex; flex-direction: column; align-items: center; }

  .card-band { left: 119px; top: 786px; }
  .card-band .centre-stack { top: 225px; gap: 18px; }
  .card-band .contact-line { margin-top: 4px; }

  .card-footer { left: 130px; top: 1487px; }
  .card-footer .centre-stack { top: 260px; gap: 20px; }
  .footer-band { position: absolute; left: 0; bottom: 0; width: 100%; height: 109px; background: var(--teal); display: flex; align-items: center; justify-content: center; gap: 40px; }
  .footer-band .contact-line { font-family: "Oswald", sans-serif; font-weight: 500; font-size: 38px; color: #fff; }
  .footer-band .contact-icon path, .footer-band .contact-icon rect { stroke: #fff; }
  .footer-band .contact-icon { width: 36px; height: 32px; }
</style>
</head>
<body>

<div class="option-number" style="top:362px">1</div>
<div class="option-number" style="top:1070px">2</div>
<div class="option-number" style="top:1780px">3</div>

<!-- Option 1: wave card -->
<section class="card card-wave">
  <svg class="wave" viewBox="0 0 964 595" preserveAspectRatio="none" aria-hidden="true">
    <path d="M0,360 C50,400 150,425 300,428 C170,438 60,420 0,398 Z" fill="var(--swoosh)"/>
    <path d="M330,410 C560,360 790,335 964,372 L964,382 C800,350 580,372 330,410 Z" fill="var(--teal)"/>
    <path d="M0,418 C180,465 340,448 520,412 C700,378 850,372 964,390 L964,595 L0,595 Z" fill="var(--teal)"/>
  </svg>
  <div class="details">
    <div class="holder-name">Derek Hollis</div>
    <div class="brand-line">
      <span class="brand-mark"><span class="brand-square"></span>Brenhurst</span>
      <span class="brand-role">Specialist</span>
    </div>
    <div class="contact-line">
      <svg class="contact-icon" viewBox="0 0 30 26"><rect x="2" y="5" width="26" height="17"/><path d="M2,5 L15,15 L28,5"/></svg>
      quellinheating@mailvora.net
    </div>
    <div class="contact-line">
      <svg class="contact-icon" viewBox="0 0 30 26"><rect x="8" y="2" width="14" height="22" rx="2"/><path d="M8,19 L22,19"/></svg>
      07832 480917
    </div>
  </div>
  <div class="company-name">Quellin Heating and Plumbing</div>
</section>

<!-- Option 2: header band card -->
<section class="card card-band">
  <div class="header-band"><div class="company-name">Quellin Heating and Plumbing</div></div>
  <div class="centre-stack">
    <div class="holder-name">Derek Hollis</div>
    <div class="brand-line">
      <span class="brand-mark"><span class="brand-square"></span>Brenhurst</span>
      <span class="brand-role">Specialist</span>
    </div>
    <div class="contact-line">
      <svg class="contact-icon" viewBox="0 0 30 26"><rect x="2" y="5" width="26" height="17"/><path d="M2,5 L15,15 L28,5"/></svg>
      quellinheating@mailvora.net
    </div>
    <div class="contact-line">
      <svg class="contact-icon" viewBox="0 0 30 26"><rect x="8" y="2" width="14" height="22" rx="2"/><path d="M8,19 L22,19"/></svg>
      07832 480917
    </div>
  </div>
</section>

<!-- Option 3: header and footer band card -->
<section class="card card-footer">
  <div class="header-band"><div class="company-name">Quellin Heating and Plumbing</div></div>
  <div class="centre-stack">
    <div class="holder-name">Derek Hollis</div>
    <div class="brand-line">
      <span class="brand-mark"><span class="brand-square"></span>Brenhurst</span>
      <span class="brand-role">Specialist</span>
    </div>
  </div>
  <div class="footer-band">
    <div class="contact-line">
      <svg class="contact-icon" viewBox="0 0 30 26"><rect x="2" y="5" width="26" height="17"/><path d="M2,5 L15,15 L28,5"/></svg>
      quellinheating@mailvora.net
    </div>
    <div class="contact-line">
      <svg class="contact-icon" viewBox="0 0 30 26"><rect x="8" y="2" width="14" height="22" rx="2"/><path d="M8,19 L22,19"/></svg>
      07832 480917
    </div>
  </div>
</section>

</body>
</html>
```